Start Up Business Launcher needs a business card

We need a business card logo and word design for a new company called Varnquist Ventures. We are a company dedicated to creating, testing, and developing, a myriad of repeatable and scalable business models (start ups) through innovative and consistent application of knowledge and expertise.

Target Market(s)

We test the marketability of start ups to various clientelle

Industry/Entity Type

Startup

Contact Information for Business Card

Varnquist Ventures
Milo Hartwin LL.B, MBA.
Founder and President
#402 118 27 Ave NE Calgary AB
varnquistventures@mailbox-demo.net
(403) 555-0193

Colors

Designer to choose colors to be used in the design.

Requirements
Must have
• A logo for Varnquist Ventures and a stylized written logo for Varnquist Ventures
Nice to have
• bold design that demonstrates professionalism, consistency, and innovation.

```html
<!DOCTYPE html>
<html lang="en">
<head>
<meta charset="utf-8">
<title>Varnquist Ventures — Business Card</title>
<link rel="stylesheet" href="https://fonts.googleapis.com/css2?family=Montserrat:wght@400;500&family=Open+Sans:wght@700&display=swap">
<style>
  :root {
    --stage: #8a8a8a;
    --navy: #1a3358;
    --blue: #1b8fd6;
    --green: #4cb848;
    --white: #ffffff;
  }
  * { box-sizing: border-box; margin: 0; padding: 0; }
  html, body { width: 1056px; height: 1200px; overflow: hidden; }
  body { background: var(--stage); position: relative; font-family: "Montserrat", sans-serif; }

  .card { position: absolute; left: 26px; width: 1008px; overflow: hidden; }
  .card-front { top: 20px; height: 570px; background: var(--navy); border-radius: 0 0 16px 16px; }
  .card-back { top: 606px; height: 574px; background: var(--white); }

  .front-shapes { position: absolute; inset: 0; }

  .holder { position: absolute; left: 44px; top: 62px; color: var(--blue); }
  .holder-name { font-size: 30px; font-weight: 400; letter-spacing: 0.5px; }
  .holder-rule { width: 148px; height: 4px; background: var(--blue); margin: 14px 0 18px; }
  .holder-title { font-size: 27px; font-weight: 400; }

  .contact { position: absolute; left: 536px; top: 30px; list-style: none; }
  .contact-item { display: flex; align-items: center; height: 56px; margin-bottom: 30px; }
  .contact-icon { width: 56px; height: 56px; border-radius: 50%; background: var(--white); display: flex; align-items: center; justify-content: center; flex: none; }
  .contact-text { margin-left: 26px; font-family: "Open Sans", sans-serif; font-weight: 700; font-size: 19px; line-height: 1.55; color: var(--white); }

  .brand { position: absolute; display: flex; align-items: center; }
  .brand-square { background: var(--blue); flex: none; }
  .brand-divider { background: var(--blue); flex: none; }
  .brand-name { font-family: "Montserrat", sans-serif; font-weight: 500; color: var(--blue); text-transform: uppercase; white-space: nowrap; line-height: 1.15; }
  .brand-line { display: block; }

  .brand-front { left: 110px; top: 318px; }
  .brand-front .brand-square { width: 80px; height: 80px; }
  .brand-front .brand-divider { width: 2px; height: 136px; margin: 0 34px; }
  .brand-front .brand-name { font-size: 34px; letter-spacing: 6px; }

  .brand-back { left: 0; right: 0; top: 0; bottom: 0; justify-content: center; }
  .brand-back .brand-square { width: 132px; height: 132px; }
  .brand-back .brand-divider { width: 3px; height: 190px; margin: 0 54px; }
  .brand-back .brand-name { font-size: 50px; letter-spacing: 9px; }
</style>
</head>
<body>

<section class="card card-front">
  <svg class="front-shapes" width="1008" height="570" viewBox="0 0 1008 570" aria-hidden="true">
    <polygon points="0,518 1008,438 1008,570 0,570" fill="var(--blue)"/>
    <polygon points="454,530 1008,378 1008,448" fill="var(--green)"/>
    <polygon points="0,280 938,324 938,438 0,500" fill="var(--white)"/>
  </svg>

  <div class="holder">
    <p class="holder-name">Milo Hartwin LL.B, MBA.</p>
    <div class="holder-rule"></div>
    <p class="holder-title">Founder &amp; President</p>
  </div>

  <ul class="contact">
    <li class="contact-item">
      <span class="contact-icon">
        <svg width="22" height="30" viewBox="0 0 22 30" aria-hidden="true"><path d="M11 0C4.9 0 0 4.9 0 11c0 8 11 19 11 19s11-11 11-19C22 4.9 17.1 0 11 0zm0 15.5a4.5 4.5 0 1 1 0-9 4.5 4.5 0 0 1 0 9z" fill="var(--navy)"/></svg>
      </span>
      <p class="contact-text">#402 118 27 Ave NE<br>Calgary AB</p>
    </li>
    <li class="contact-item">
      <span class="contact-icon">
        <svg width="28" height="20" viewBox="0 0 28 20" aria-hidden="true"><rect x="1.5" y="1.5" width="25" height="17" fill="none" stroke="var(--navy)" stroke-width="3"/><path d="M2 2l12 10L26 2M2 18l9-8M26 18l-9-8" fill="none" stroke="var(--navy)" stroke-width="2.5"/></svg>
      </span>
      <p class="contact-text">varnquistventures@mailbox-demo.net</p>
    </li>
    <li class="contact-item">
      <span class="contact-icon">
        <svg width="26" height="26" viewBox="0 0 24 24" aria-hidden="true"><path d="M6.6 10.8a15.1 15.1 0 0 0 6.6 6.6l2.2-2.2c.3-.3.7-.4 1-.2 1.1.4 2.3.6 3.6.6.6 0 1 .4 1 1V20c0 .6-.4 1-1 1A17 17 0 0 1 3 4c0-.6.4-1 1-1h3.5c.6 0 1 .4 1 1 0 1.3.2 2.5.6 3.6.1.3 0 .7-.2 1z" fill="var(--navy)"/></svg>
      </span>
      <p class="contact-text">(403) 555-0193</p>
    </li>
  </ul>

  <div class="brand brand-front">
    <span class="brand-square"></span>
    <span class="brand-divider"></span>
    <p class="brand-name"><span class="brand-line">Varnquist</span><span class="brand-line">Ventures</span></p>
  </div>
</section>

<section class="card card-back">
  <div class="brand brand-back">
    <span class="brand-square"></span>
    <span class="brand-divider"></span>
    <p class="brand-name"><span class="brand-line">Varnquist</span><span class="brand-line">Ventures</span></p>
  </div>
</section>

</body>
</html>
```